Quote Cards for Social Media KL

I would like to put these quotes over one of the pictures attached; One Quote per picture, and I want the quote to be bold or easy to read as well. I provided a few reference graphics that I really like as examples below. In very small letters at the bottom add @KLVarneyDaily

All of the pictures are attached; you can pick any photo and add one quote to it; but no stock photography

Target Market(s)

women trying to lose weight

Requirements
Must have
• quotes and pictures attached
Should not have
• no stock photography

```html
<!DOCTYPE html>
<html lang="en">
<head>
<meta charset="utf-8">
<title>Quote Cards — KL</title>
<link rel="stylesheet" href="https://fonts.googleapis.com/css2?family=Barlow+Condensed:wght@600&family=Dancing+Script:wght@600&display=swap">
<style>
  :root {
    --canvas: #000000;
    --quote: #ffffff;
    --shadow: rgba(0, 0, 0, 0.55);
  }
  * { margin: 0; padding: 0; box-sizing: border-box; }
  html, body { width: 1200px; height: 896px; overflow: hidden; background: var(--canvas); }
  .board { position: relative; width: 1200px; height: 896px; }
  .card {
    position: absolute;
    width: 268px;
    height: 268px;
    overflow: hidden;
  }
  .card-photo { position: absolute; inset: 0; }
  .quote {
    position: absolute;
    left: 0; right: 0;
    text-align: center;
    font-family: "Barlow Condensed", sans-serif;
    font-weight: 600;
    font-size: 18.5px;
    line-height: 20.3px;
    color: var(--quote);
    text-transform: uppercase;
    text-shadow: 0 1px 3px var(--shadow), 0 0 6px var(--shadow);
  }
  .handle {
    position: absolute;
    left: 0; right: 0;
    text-align: center;
    font-family: "Dancing Script", cursive;
    font-weight: 600;
    font-size: 9.5px;
    color: var(--quote);
    text-shadow: 0 1px 2px var(--shadow);
  }
  .c1 { left: 24px;  top: 21px; }
  .c2 { left: 318px; top: 21px; }
  .c3 { left: 612px; top: 21px; }
  .c4 { left: 906px; top: 21px; }
  .c5 { left: 24px;  top: 310px; }
  .c6 { left: 318px; top: 310px; }
  .c7 { left: 612px; top: 310px; }
  .c8 { left: 906px; top: 310px; }
  .c9 { left: 318px; top: 604px; }
  .c10 { left: 612px; top: 604px; }

  .c1 .card-photo { background: linear-gradient(135deg, #e2562c 0%, #c2309a 45%, #6a2b8e 75%, #3a1e55 100%); }
  .c2 .card-photo { background: linear-gradient(180deg, #e8dfd3 0%, #c89c72 55%, #8a5b39 100%); }
  .c3 .card-photo { background: linear-gradient(180deg, #9fbdd6 0%, #6f8060 35%, #2c3121 70%, #16160f 100%); }
  .c4 .card-photo { background: linear-gradient(90deg, #eae6e2 0%, #d8d2cc 45%, #7a3ca6 75%, #3b2a3a 100%); }
  .c5 .card-photo { background: linear-gradient(135deg, #4d2fb0 0%, #8a2fa6 45%, #b84a7e 70%, #432075 100%); }
  .c6 .card-photo { background: linear-gradient(90deg, #2d2d2f 0%, #dad8d5 40%, #cfcac6 60%, #3a3636 100%); }
  .c7 .card-photo { background: linear-gradient(90deg, #2a2a2c 0%, #d6d3cf 40%, #bfb9b3 65%, #262323 100%); }
  .c8 .card-photo { background: linear-gradient(180deg, #e6e7e8 0%, #c7c6c4 55%, #56524e 100%); }
  .c9 .card-photo { background: linear-gradient(180deg, #1e2a4a 0%, #7d6a58 50%, #c9a33a 85%, #8b6a1a 100%); }
  .c10 .card-photo { background: linear-gradient(160deg, #2a2623 0%, #5a463a 45%, #2a211c 75%, #a58e78 100%); }
</style>
</head>
<body>
<main class="board">

  <article class="card c1">
    <div class="card-photo" role="img" aria-label="Photo of the woman in a pink gown on a brightly lit orange and purple stage"></div>
    <p class="quote" style="top:113px">Wake up tomorrow<br>with a flatter belly- yes,<br>this overnight remedy<br>works like magic!</p>
    <p class="handle" style="top:209px">@KLVarneyDaily</p>
  </article>

  <article class="card c2">
    <div class="card-photo" role="img" aria-label="Photo of the woman smiling in a camel turtleneck against a light wall"></div>
    <p class="quote" style="top:119px">One supplement,<br>one night; your belly bloat<br>could be gone<br>by morning. Here's<br>how it works!</p>
    <p class="handle" style="top:222px">@KLVarneyDaily</p>
  </article>

  <article class="card c3">
    <div class="card-photo" role="img" aria-label="Photo of the woman in black on a terrace with green hills behind"></div>
    <p class="quote" style="top:120px">A natural way to<br>boost GLP-1 - no injections,<br>no side effects,<br>just real results.<br>Here's how it works</p>
    <p class="handle" style="top:222px">@KLVarneyDaily</p>
  </article>

  <article class="card c4">
    <div class="card-photo" role="img" aria-label="Photo of the woman in a purple dress at an awards event beside white shelving"></div>
    <p class="quote" style="top:151px">That stubborn belly fat<br>isn't your fault - here's what<br>no one tells you.</p>
    <p class="handle" style="top:222px">@KLVarneyDaily</p>
  </article>

  <article class="card c5">
    <div class="card-photo" role="img" aria-label="Photo of the woman posing beside a giant basketball under purple light"></div>
    <p class="quote" style="top:118px">GLP-1: The magic behind the<br>weight loss drugs.<br>But here's the secret<br>you can boost it naturally<br>without a prescription!</p>
    <p class="handle" style="top:223px">@KLVarneyDaily</p>
  </article>

  <article class="card c6">
    <div class="card-photo" role="img" aria-label="Photo of the woman dancing in a sheer black top in a bright apartment"></div>
    <p class="quote" style="top:114px">Frustrated with belly fat<br>that won't budge? I've<br>got the solution that<br>finally worked for me-no<br>crazy diets required.</p>
    <p class="handle" style="top:223px">@KLVarneyDaily</p>
  </article>

  <article class="card c7">
    <div class="card-photo" role="img" aria-label="Photo of the woman smiling in a striped sheer black top in an apartment"></div>
    <p class="quote" style="top:152px">Sis, your hormones are<br>out of whack - that's<br>why the weight won't budge!</p>
    <p class="handle" style="top:223px">@KLVarneyDaily</p>
  </article>

  <article class="card c8">
    <div class="card-photo" role="img" aria-label="Photo of the woman dancing in a white sweater in a modern kitchen"></div>
    <p class="quote" style="top:134px">Finally-a natural<br>solution that flattens<br>your belly and eases<br>stomach bloat</p>
    <p class="handle" style="top:223px">@KLVarneyDaily</p>
  </article>

  <article class="card c9">
    <div class="card-photo" role="img" aria-label="Photo of the woman in a brown sparkly top standing courtside in an arena"></div>
    <p class="quote" style="top:154px">You've been lied to<br>'just eat less and exercise more'<br>doesn't work in menopause</p>
    <p class="handle" style="top:223px">@KLVarneyDaily</p>
  </article>

  <article class="card c10">
    <div class="card-photo" role="img" aria-label="Photo of the woman in a black top in a dim living room at night"></div>
    <p class="quote" style="top:114px">Struggling with bloating<br>and belly fat? Try this<br>natural solution tonight,<br>and wake up feeling lighter!</p>
    <p class="handle" style="top:210px">@KLVarneyDaily</p>
  </article>

</main>
</body>
</html>
```